Bright Harbor Realty

We need a good looking flyer for our real estate company to impress people who are considering to sell their homes for as low as 1.5% listing commission. Please see flyer examples for reference.
555-318-4096
Real Estate

```html
<!DOCTYPE html>
<html lang="en">
<head>
<meta charset="utf-8">
<title>Bright Harbor Realty – Just Sold Flyer</title>
<link rel="stylesheet" href="https://fonts.googleapis.com/css2?family=Arimo:wght@400;700&display=swap">
<style>
  :root {
    --page-bg: #2b2b2b;
    --header-bg: #ffffff;
    --skyline-light: #f4f4f4;
    --skyline-tone: #d9d9d9;
    --brand-blue: #1f4fa3;
    --flyer-blue: #2e6fb8;
    --flyer-blue-dark: #1d5a9c;
    --flyer-blue-light: #4a8fd0;
    --accent-yellow: #ffe600;
    --tag-yellow: #ffe91a;
    --tag-red: #e0262b;
    --caption-bg: #3b3b3b;
    --caption-text: #f2f2f2;
    --white: #ffffff;
    --photo-sky: #9cc3e4;
    --photo-grass: #5f9a3c;
  }
  * { box-sizing: border-box; margin: 0; padding: 0; }
  html, body { width: 1200px; height: 714px; overflow: hidden; background: var(--page-bg); }
  .canvas { position: relative; width: 1200px; height: 714px; overflow: hidden; }
  .flyer {
    position: absolute; left: 347px; top: 0;
    width: 590px; height: 833px;
    transform: scale(0.8572); transform-origin: top left;
    font-family: "Arimo", Arial, sans-serif;
    background: linear-gradient(160deg, var(--flyer-blue-light) 0%, var(--flyer-blue) 40%, var(--flyer-blue-dark) 75%, var(--flyer-blue) 100%);
    overflow: hidden;
  }
  .header { position: absolute; left: 0; top: 0; width: 590px; height: 201px; background: var(--header-bg); }
  .skyline {
    position: absolute; left: 0; top: 0; width: 590px; height: 201px;
    background:
      linear-gradient(180deg, rgba(255,255,255,0.9) 0%, rgba(255,255,255,0) 35%),
      linear-gradient(90deg, var(--skyline-tone) 0%, var(--skyline-light) 20%, var(--skyline-tone) 45%, var(--skyline-light) 70%, var(--skyline-tone) 100%);
  }
  .agent-photo {
    position: absolute; right: 0; top: 0; width: 190px; height: 201px;
    background: linear-gradient(180deg, #d8d8d8 0%, #8a6a55 35%, #3a3a3a 65%, #1e1e1e 100%);
  }
  .brand {
    position: absolute; left: 40px; top: 62px; width: 330px;
    display: flex; flex-direction: column; align-items: center; gap: 10px;
    color: var(--brand-blue); font-weight: 700; text-align: center;
  }
  .brand-mark { width: 44px; height: 44px; background: var(--brand-blue); }
  .brand-name { font-size: 34px; line-height: 36px; }
  .tag { position: absolute; left: 220px; top: 195px; width: 370px; height: 170px; }
  .headline {
    position: absolute; left: 18px; top: 262px;
    color: var(--accent-yellow); font-size: 22px; line-height: 28px;
  }
  .listing { position: absolute; width: 177px; height: 156px; }
  .listing-photo {
    height: 118px;
    background: linear-gradient(180deg, var(--photo-sky) 0%, #dfe8ef 45%, #cfcfc8 60%, var(--photo-grass) 100%);
  }
  .listing-caption {
    height: 38px; background: var(--caption-bg); color: var(--caption-text);
    font-size: 9.5px; line-height: 13px; text-align: center; padding-top: 6px;
  }
  .did-you-know {
    position: absolute; left: 0; top: 704px; width: 590px; text-align: center;
    color: var(--accent-yellow); font-weight: 700; font-size: 23px; line-height: 26px;
  }
  .savings-note {
    position: absolute; left: 20px; top: 731px; width: 550px; text-align: center;
    color: var(--white); font-size: 13.5px; line-height: 16px;
  }
  .call-to-action {
    position: absolute; left: 0; top: 777px; width: 590px; text-align: center;
    color: var(--white); font-weight: 700; font-size: 14px; line-height: 16px;
  }
  .phone {
    position: absolute; left: 0; top: 792px; width: 590px; text-align: center;
    color: var(--accent-yellow); font-weight: 700; font-size: 27px; line-height: 32px;
  }
</style>
</head>
<body>
<div class="canvas">
  <div class="flyer">
    <header class="header">
      <div class="skyline" role="img" aria-label="Line drawing of a city skyline"></div>
      <div class="agent-photo" role="img" aria-label="Portrait photo of the listing agent in a dark suit"></div>
      <div class="brand">
        <span class="brand-mark"></span>
        <span class="brand-name">Bright Harbor<br>Realty</span>
      </div>
    </header>

    <svg class="tag" viewBox="0 0 370 170" role="img" aria-label="Just Sold price tag">
      <path d="M12 0 C 20 30, 40 40, 140 62" stroke="#ffffff" stroke-width="2" fill="none"/>
      <g transform="rotate(12 235 85)">
        <path d="M110 40 L335 40 Q348 40 348 53 L348 127 Q348 140 335 140 L110 140 L80 90 Z"
              fill="var(--tag-yellow)" stroke="var(--tag-red)" stroke-width="3"/>
        <circle cx="105" cy="90" r="11" fill="#ffffff" stroke="var(--tag-red)" stroke-width="3"/>
        <text x="228" y="86" text-anchor="middle" font-family="Arimo, Arial, sans-serif" font-weight="700" font-size="46" fill="var(--tag-red)">JUST</text>
        <text x="228" y="132" text-anchor="middle" font-family="Arimo, Arial, sans-serif" font-weight="700" font-size="46" fill="var(--tag-red)">SOLD</text>
      </g>
    </svg>

    <p class="headline">List For 1.5 Commission,<br>Still Receive Top Marketing!</p>

    <article class="listing" style="left:16px; top:368px;">
      <div class="listing-photo" role="img" aria-label="Photo of a single-story home with palm trees"></div>
      <p class="listing-caption">1420 Maple Cove Circle<br>Harborview, FL 33400 - $250,000</p>
    </article>
    <article class="listing" style="left:209px; top:368px;">
      <div class="listing-photo" role="img" aria-label="Photo of a gray single-story home and lawn"></div>
      <p class="listing-caption">2875 E Willow Run Drive<br>Palm Hollow, FL 33401 - $280,000</p>
    </article>
    <article class="listing" style="left:397px; top:368px;">
      <div class="listing-photo" role="img" aria-label="Photo of a home with carport and driveway"></div>
      <p class="listing-caption">3318 Laurel Bend Circle<br>Harborview, FL 33400 - $335,000</p>
    </article>
    <article class="listing" style="left:16px; top:537px;">
      <div class="listing-photo" role="img" aria-label="Photo of a two-story home with garage"></div>
      <p class="listing-caption">4106 Seabreeze Circle E<br>Coral Point, FL 33402 - $229,500</p>
    </article>
    <article class="listing" style="left:209px; top:537px;">
      <div class="listing-photo" role="img" aria-label="Photo of a green home with garage among trees"></div>
      <p class="listing-caption">517 S Fairway Club Drive<br>Bay Crest, FL 33403 - $550,000</p>
    </article>
    <article class="listing" style="left:397px; top:537px;">
      <div class="listing-photo" role="img" aria-label="Photo of a two-story home with garage"></div>
      <p class="listing-caption">1420 Maple Cove Circle<br>Harborview, FL 33400 - $250,000</p>
    </article>

    <h2 class="did-you-know">Did You Know?</h2>
    <p class="savings-note">On average, our customers save $8,750 when they choose us.... and they still receive top marketing, srvice and representation!</p>
    <p class="call-to-action">Call Us Today and Save Thousands!</p>
    <p class="phone">(555) 318-4096</p>
  </div>
</div>
</body>
</html>
```